Flyer Design Project for Harbor Tidy Works Inc.

We require a double sided marketing flyer 8 1/2 x 11. The flyer will also be marketed via e-mail using one or both sides. "Outside of the box" but yet "professional" marketing is what we'd like to achieve.

Harbor Tidy Works Inc., is a building service company providing cleaning, caretaking and concierge service to residential/stratas (condominiums/apartments)...(These services are usually provided during daytime hours). and janitorial service to commercial buildings ( service provided at night time).

- 100% green cleaning chemicals and systems
- Professionally trained staff
- Customer service is #1 priority
- Excellent Communication systems

Brochure to be 2 pages.:

Side 1: marketing residential/strata building services with a focus on providing cleaning services with a sub-focus on caretaking and concierge. We also provide move-in/out service where we coordinate with tenants to arrange access to the building, elevators and provide security (no moving involved)

Side 2: marketing night time janitorial service to property managers, corporate head offices, small offices, industrial facilities

http://www.gleamnest-home.com/index.php

http://www.brightholdpc.ca/services

These websites are from the best maid cleaning business and best strata//residential cleaning business in the city. The maid website is "you" focused, that works! The other is very straight forward and to the point, which also works.

At the end of the day our target audience ( property managers and building owners ) want us to take away one of their biggest headaches - "CLEANING". They have better things to be doing than dealing with whether or not the elevator is clean! That's our job! We're in the CLEANING business and when they don't hear a word from any of their tenants, we're doing our job and they're HAPPY :) WE TAKE AWAY HEADACHES AND MAKE PEOPLE HAPPY!

very multi-cultural target audience!

HOW CAN WE SHOW THEM IN A FLYER? THAT'S THE CHALLENGE! AND THE WINNING DESIGNER WILL BE THE ONE WHO CAN EFFECTIVELY COMMUNICATE THIS IN 1-2 PAGES.
Updates

Thank you all very much. Varolinda and Tulip, your designs are very encouraging.

Design 1223617: The layout is close to what we are hoping to achieve as it may also be incorporated into a web site homepage with each block used as a link to more info. The pictures however, make it look like any other company flyer.

Design 1224020: Also a very good layout but again not liking the pictures.

Overall, some of the designs are a little to busy with information. I would like to see something just a little more simple and yet unique that stands out against other companies.

Look forward to the second round. Thank you all very much!

Please see the new files called commercial building pics, residential strata pics and misc pics that you can use in the brochure. These are the types of pictures I would like included. Thanks.

Hi Designers

Would like to see a design that combines the layout format of the bottom half of 1234602 ( easy to read) and the top half of 1227356 ( like the pictures in this one).

Also, want to replace "Marketing....." with Side #1 " Providing residential/stratas with quality, affordable cleaning, caretaking and concierge services.. and then the rest of the text in point/bullet form.

With side #2, want to replace " Marketing...." with "Providing quality, affordable commercial janitorial service to....

                                   

 

Please use latest pictures uploaded. The designs we've liked so far have 1 large picture ( picture of buildings ) on each side with 2-3 smaller pics in various layouts. i.e. for side 1 : Cleaning ( a picture of a cleaner ) Caretaking ( picture of handyman in white shaking hand) Concierge ( picture of person at a desk on the phone)

The font should be large and easy to read. We also like the designs where key points are in point form.

The company name and logo and contact info should be easy to read.

We did like one design using vector characters but think they should only be incorporated as part of the overall design

Target Market(s)

Property Managers, Building Owners, Multicultural Decision makers, aged 28 - 60, very busy people

Industry/Entity Type

Janitorial Service

Requirements
Must have
• 2 pages, 8 1/2 x 11 ( double sided) but can be used separately
Nice to have
• Would like to be able to change photos for different campaigns

```html
<!DOCTYPE html>
<html lang="en">
<head>
<meta charset="utf-8">
<title>Harbor Tidy Works Inc. – Flyer</title>
<link href="https://fonts.googleapis.com/css2?family=Open+Sans:ital,wght@0,400;0,600;0,700;1,700&display=swap" rel="stylesheet">
<style>
:root{
  --green:#8dc63f;
  --green-dark:#6fa82b;
  --ink:#231f20;
  --text:#3a3a3a;
  --paper:#ffffff;
  --backdrop:#e6e4df;
  --sky-top:#2f6fb5;
  --sky-bottom:#a9cbe8;
  --glass:#5f8fa3;
}
*{box-sizing:border-box;margin:0;padding:0}
html,body{width:1200px;height:791px;overflow:hidden}
body{background:var(--backdrop);font-family:"Open Sans",Arial,sans-serif;color:var(--text);position:relative}
.page{position:absolute;top:62px;width:517px;height:668px;background:var(--paper);overflow:hidden}
.page--residential{left:62px}
.page--commercial{left:622px}
.photo{position:absolute}
.photo--tower{left:0;top:0;width:226px;height:244px;background:linear-gradient(160deg,var(--sky-top),var(--sky-bottom) 55%,#9fb4c0)}
.photo--highrise{left:295px;top:270px;width:221px;height:250px;background:linear-gradient(170deg,var(--sky-top),#6e9fd0 40%,#d8dde2 70%,#7f8c99)}
.photo--glass{left:0;top:0;width:226px;height:286px;background:linear-gradient(200deg,var(--sky-bottom),var(--glass) 45%,#2f5f6e)}
.brand{position:absolute;left:226px;width:290px;top:60px;display:flex;align-items:center;justify-content:center;gap:10px}
.brand__dot{width:22px;height:22px;border-radius:50%;background:var(--green)}
.brand__name{font-size:38px;font-weight:400;color:var(--ink);letter-spacing:-.5px}
.tagline{position:absolute;left:226px;width:290px;top:143px;text-align:center;font-size:10px;font-weight:700;font-style:italic;color:var(--ink)}
.intro{position:absolute;left:226px;top:168px;width:290px;height:76px;background:var(--green);color:#fff;font-size:8.3px;line-height:1.35;padding:3px 6px}
.intro--headline{font-size:13.5px;line-height:1.55;text-align:center;padding:3px 4px;color:#1f2a12}
.pointer{position:absolute;width:0;height:0;border-left:7px solid transparent;border-right:7px solid transparent;border-top:12px solid var(--green)}
.services{position:absolute;left:4px;top:256px;display:flex;gap:38px;font-size:8.5px;font-weight:700;font-style:italic;color:var(--ink)}
.banner{position:absolute;left:0;display:flex;align-items:center;color:#fff;font-weight:700;font-style:italic;font-size:10.5px;line-height:1.25;padding-left:14px}
.banner::before{content:"";position:absolute;inset:0;background:var(--green);clip-path:polygon(0 0,100% 0,calc(100% - 14px) 100%,0 100%);z-index:0}
.banner::after{content:"";position:absolute;top:0;bottom:0;right:-22px;width:20px;background:var(--ink);clip-path:polygon(14px 0,100% 0,6px 100%,0 100%)}
.banner span{position:relative;z-index:1}
.banner--dark-text span{color:var(--ink)}
.bullets{position:absolute;list-style:none;font-size:7.3px;line-height:14.2px;color:var(--text)}
.bullets li{padding-left:14px;position:relative}
.bullets li::before{content:"";position:absolute;left:0;top:5px;width:5px;height:5px;background:var(--ink)}
.contact-card{position:absolute;left:300px;top:544px;width:200px;height:106px;background:var(--ink);border-radius:14px;color:#fff;text-align:center;padding-top:8px}
.contact-card__name{font-size:11px;font-weight:700;font-style:italic}
.contact-card__address{font-size:8.5px;line-height:1.35;margin-top:6px}
.contact-card__phone{font-size:11px;font-weight:700;font-style:italic;margin-top:9px}
.contact-card__email{font-size:11px;font-weight:700;font-style:italic;margin-top:9px}
.feature{position:absolute;top:304px;height:120px;background:var(--green);padding:8px 8px}
.feature ul{list-style:none;font-size:9px;line-height:1.25;color:#1f2a12}
.feature li{position:relative;padding-left:14px;margin-bottom:6px}
.feature li::before{content:"";position:absolute;left:0;top:3px;width:6px;height:6px;background:var(--ink)}
.feature--a{left:0;width:148px}
.feature--b{left:154px;width:158px;padding-top:14px}
.feature--b li{margin-bottom:19px}
.feature--c{left:318px;width:199px;padding-top:12px}
.feature--c li{margin-bottom:8px}
.body-copy{position:absolute;left:16px;top:470px;width:490px;font-size:8.3px;line-height:1.5;color:var(--text)}
.footer{position:absolute;left:0;top:614px;width:517px;height:54px;background:var(--ink);color:#fff}
.footer__name{position:absolute;left:16px;top:8px;font-size:11.5px;font-weight:700;font-style:italic;line-height:1.45}
.footer__address{position:absolute;right:14px;top:4px;font-size:11px;text-align:right}
.footer__contact{position:absolute;right:14px;top:22px;font-size:12px;font-weight:700;font-style:italic}
</style>
</head>
<body>

<section class="page page--residential">
  <div class="photo photo--tower" role="img" aria-label="Photo of a curved glass residential tower against a blue sky"></div>
  <div class="brand"><span class="brand__dot"></span><span class="brand__name">harbor tidy</span></div>
  <p class="tagline">WE TAKE AWAY HEADACHES AND MAKE PEOPLE HAPPY!</p>
  <p class="intro">Our Company is a building service company providing cleaning, caretaking and concierge service to residential / stratas (condominiums / apartments)... (These services are usually provided during daytime hours). and janitorial service to commercial buildings ( service provided at night time). 100% green cleaning chemicals and systems. Focus on customer service and communication.</p>
  <div class="pointer" style="left:349px;top:244px"></div>

  <div class="services"><span>■CLEANING</span><span>■CARETAKING</span><span>■CONCIERGE</span></div>

  <div class="banner" style="top:277px;width:215px;height:33px"><span># 1 PRIORITY - CUSTOMER SERVICE<br>And communication</span></div>
  <div class="banner" style="top:313px;width:270px;height:31px"><span>OVER 20 YEARS INDUSTRY EXPERIENCE TRAINED<br>COUTEOUS STAFF</span></div>
  <div class="banner" style="top:349px;width:150px;height:22px"><span>100% GREEN CHEMICALS</span></div>
  <div class="banner" style="top:380px;width:205px;height:33px"><span>Servicing greater vancouver<br>AFFORDABLE, QUALITY SERVICE</span></div>
  <div class="banner" style="top:420px;width:270px;height:22px"><span>NEW CONSTRUCTION? WE DO MOVE-INS/OUTS</span></div>
  <div class="banner banner--dark-text" style="top:447px;width:116px;height:20px"><span>Brighthold Service</span></div>

  <ul class="bullets" style="left:14px;top:471px">
    <li>Daily, weekly, monthly and yearly cleaning services</li>
    <li>Initial cleaning / one-time jobs</li>
    <li>Project work / all types of floor maintenance</li>
    <li>Caretaker and building management services</li>
    <li>Monthly building reports and audits</li>
  </ul>

  <div class="banner banner--dark-text" style="top:547px;width:240px;height:22px"><span>Supplementary Service Packages include:</span></div>
  <ul class="bullets" style="left:14px;top:569px">
    <li>Window cleaning</li>
    <li>Pressure washing</li>
    <li>Carpet cleaning</li>
    <li>Waste/Garbage removal</li>
    <li>Special events cleaning</li>
    <li>Lighting maintenance</li>
  </ul>

  <div class="photo photo--highrise" role="img" aria-label="Photo of a white high-rise apartment building seen from below"></div>

  <address class="contact-card" style="font-style:normal">
    <p class="contact-card__name">Harbor Tidy Works Inc.</p>
    <p class="contact-card__address">1234, Street Name, State Name,<br>Country Name, Country Name,</p>
    <p class="contact-card__phone">CALL 604-555-0148</p>
    <p class="contact-card__email">dale@harbortidyworks.com</p>
  </address>
</section>

<section class="page page--commercial">
  <div class="photo photo--glass" role="img" aria-label="Photo of a glass office tower rising into a blue sky"></div>
  <div class="brand"><span class="brand__dot"></span><span class="brand__name">harbor tidy</span></div>
  <p class="tagline">WE TAKE AWAY HEADACHES AND MAKE PEOPLE HAPPY!</p>
  <p class="intro intro--headline">Marketing Night Time Janitorial Service to Property Managers, Corporate Head Offices, Small Offices, Industrial Facilities</p>
  <div class="pointer" style="left:351px;top:244px"></div>

  <div class="feature feature--a"><ul>
    <li>CUSTOMIZED SPECIFICATIONS</li>
    <li>STRUCTURED SUPERVISION</li>
    <li>24/7</li>
    <li>SYSTEMATIC QUALITY ASSURANCE (QA) AUDITS</li>
  </ul></div>
  <div class="feature feature--b"><ul>
    <li>DAILY OR WEEKLY SERVICE</li>
    <li>500 – 200,00 SQUARE FEET</li>
    <li>100% GREEN CLEANING</li>
  </ul></div>
  <div class="feature feature--c"><ul>
    <li>NO MORE CLEANING HEADACHES!</li>
    <li>NCPA CLEANING PRODUCTION RATES</li>
    <li>20 YEARS EXPERIENCE</li>
    <li>AFFORDABLE, QUALITY SERVICE</li>
    <li>TRAINED, COURTEOUS STAFF</li>
  </ul></div>

  <div class="banner banner--dark-text" style="top:436px;width:322px;height:24px"><span>Building Management, Concierge &amp; Caretaker Services</span></div>
  <p class="body-copy">Brighthold offers building management and caretaker services responsible for the administration, repairs and cleaning of strata buildings tailored to your particular and unique requirements. For best possible service, our staff has</p>
  <ul class="bullets" style="left:16px;top:499px;font-size:8.3px;line-height:18px">
    <li>Strong and proven background in the residential strata industry</li>
    <li>Certification in pool and spa maintenance</li>
    <li>Background in small repairs</li>
    <li>Practice in dealing with trades for maximum efficiency</li>
    <li>Experience in providing written reports to property managers and strata councils</li>
    <li>Qualified support from our supervisors</li>
  </ul>

  <footer class="footer">
    <p class="footer__name">Harbor Tidy Works<br>Inc.</p>
    <p class="footer__address">1234, Street Name, State Name, Country Name, Country Name,</p>
    <p class="footer__contact">CALL 604-555-0148 Email :dale@harbortidyworks.com</p>
  </footer>
</section>

</body>
</html>
```